Brivosta Films
Creative and Dynamic Independent Films
Professional
Marcus Tollen
OWNER/PRODUCER/
47 Haldon Ave
Harlow Creek PA 17420
Marcus@BrivostaFilms.com
www.BrivostaFilms.com
Bold,Regal,Elegant
Logo File.

```html
<!DOCTYPE html>
<html lang="en">
<head>
<meta charset="utf-8">
<title>Brivosta Films — Stationery</title>
<link rel="stylesheet" href="https://fonts.googleapis.com/css2?family=Cinzel:wght@700&family=Open+Sans:wght@400;600&display=swap">
<style>
:root{
  --stage:#e9eaec;
  --panel:#2b2d31;
  --paper:#ffffff;
  --ink:#3b3f45;
  --muted:#8a9097;
  --brand:#1f6fa8;
  --brand-light:#5fb3e0;
  --brand-dark:#0f3f63;
  --flap-grey:#9a9ea4;
  --ghost:#eef0f2;
  --fold:#dcdfe2;
}
*{margin:0;padding:0;box-sizing:border-box}
html,body{width:1200px;height:343px;overflow:hidden;background:var(--stage);font-family:"Open Sans",Arial,sans-serif;color:var(--ink)}
.canvas{position:relative;width:1200px;height:343px}
.item{position:absolute;background:var(--paper);box-shadow:0 2px 6px rgba(0,0,0,.18);overflow:hidden}
.brand-mark{display:flex;align-items:center;gap:4px;font-family:"Cinzel",serif;font-weight:700;color:var(--brand-dark);white-space:nowrap}
.brand-mark .dot{border-radius:50%;background:var(--brand);flex:none}
.ghost{position:absolute;border-radius:50%;background:var(--ghost)}
.band{position:absolute;left:0;right:0;bottom:0;background:linear-gradient(90deg,var(--brand-dark),var(--brand),var(--brand-light),var(--brand),var(--brand-dark))}
.small{font-size:4px;line-height:1.4;color:var(--muted);white-space:nowrap}
.small strong{color:var(--ink);font-weight:600}

/* side panel */
.side-panel{position:absolute;left:0;top:0;width:144px;height:343px;background:var(--panel)}
.side-panel .brand-mark{position:absolute;left:18px;top:44px;font-size:15px;color:#fff}
.side-panel .brand-mark .dot{width:9px;height:9px;background:var(--brand-light)}
.side-panel .caption{position:absolute;left:34px;top:116px;font-size:7px;color:#b9bdc2}

/* business cards */
.card{left:24px;width:120px;height:70px}
.card-front{top:139px}
.card-back{top:233px}
.card .brand-mark{font-size:9px}
.card .brand-mark .dot{width:6px;height:6px}
.card-front .brand-mark{position:absolute;left:7px;top:8px}
.card-front .details{position:absolute;right:7px;top:28px;text-align:right}
.card-back .brand-mark{position:absolute;left:0;right:0;top:28px;justify-content:center}
.card .band{height:4px}

/* letterheads */
.letterhead{top:24px;width:218px;height:290px}
.letterhead-one{left:168px}
.letterhead-two{left:410px}
.letterhead .brand-mark{position:absolute;left:14px;top:14px;font-size:11px}
.letterhead .brand-mark .dot{width:8px;height:8px}
.letterhead .address{position:absolute;left:122px;top:14px}
.letterhead .ghost{left:54px;top:96px;width:110px;height:110px}
.letterhead .band{height:8px}
.letterhead .web{position:absolute;left:0;right:0;bottom:14px;text-align:center}

/* envelope fronts */
.envelope{left:641px;width:245px;height:114px}
.envelope-one{top:62px}
.envelope-two{top:199px}
.envelope .brand-mark{position:absolute;left:10px;top:10px;font-size:9px}
.envelope .brand-mark .dot{width:6px;height:6px}
.envelope .ghost{left:95px;top:12px;width:56px;height:56px}
.envelope .band{height:5px}
.envelope .web{position:absolute;left:10px;bottom:14px}

/* envelope backs */
.envelope-back{left:912px;width:280px}
.back-grey{top:56px;height:112px}
.back-blue{top:132px;height:110px}
.back-white{top:204px;height:120px}
.envelope-back svg{position:absolute;left:0;top:0}
.envelope-back .brand-mark{position:absolute;left:0;right:0;justify-content:center;font-size:7px}
.envelope-back .brand-mark .dot{width:5px;height:5px}
.back-grey .brand-mark{top:8px}
.back-blue .brand-mark{top:18px;color:#fff}
.back-blue .brand-mark .dot{background:var(--brand-light)}
.back-white .web{position:absolute;left:0;right:0;bottom:10px;text-align:center}
</style>
</head>
<body>
<main class="canvas">
  <aside class="side-panel">
    <div class="brand-mark"><span class="dot"></span>Brivosta</div>
    <p class="caption">Stationery Design</p>
  </aside>

  <section class="item card card-front">
    <div class="brand-mark"><span class="dot"></span>Brivosta</div>
    <div class="details small">
      <p><strong>Marcus Tollen</strong></p>
      <p>Owner / Producer</p>
      <p>47 Haldon Ave</p>
      <p>Harlow Creek PA 17420</p>
      <p>Marcus@BrivostaFilms.com</p>
    </div>
    <div class="band"></div>
  </section>

  <section class="item card card-back">
    <div class="brand-mark"><span class="dot"></span>Brivosta</div>
    <div class="band"></div>
  </section>

  <section class="item letterhead letterhead-one">
    <div class="brand-mark"><span class="dot"></span>Brivosta</div>
    <div class="address small">
      <p><strong>Marcus Tollen</strong></p>
      <p>47 Haldon Ave</p>
      <p>Harlow Creek PA 17420</p>
      <p>Marcus@BrivostaFilms.com</p>
    </div>
    <div class="ghost"></div>
    <p class="web small">www.BrivostaFilms.com</p>
    <div class="band"></div>
  </section>

  <section class="item letterhead letterhead-two">
    <div class="brand-mark"><span class="dot"></span>Brivosta</div>
    <div class="ghost"></div>
    <p class="web small">www.BrivostaFilms.com</p>
    <div class="band"></div>
  </section>

  <section class="item envelope envelope-one">
    <div class="brand-mark"><span class="dot"></span>Brivosta</div>
    <div class="ghost"></div>
    <p class="web small">47 Haldon Ave, Harlow Creek PA 17420</p>
    <div class="band"></div>
  </section>

  <section class="item envelope envelope-two">
    <div class="brand-mark"><span class="dot"></span>Brivosta</div>
    <div class="ghost"></div>
    <p class="web small">47 Haldon Ave, Harlow Creek PA 17420</p>
    <div class="band"></div>
  </section>

  <section class="item envelope-back back-grey">
    <svg width="280" height="112" aria-hidden="true"><polygon points="0,0 280,0 140,42" fill="var(--flap-grey)"/><polyline points="0,112 140,56 280,112" fill="none" stroke="var(--fold)"/></svg>
    <div class="brand-mark"><span class="dot"></span>Brivosta</div>
  </section>

  <section class="item envelope-back back-blue">
    <svg width="280" height="110" aria-hidden="true"><defs><linearGradient id="flap" x1="0" x2="0" y1="0" y2="1"><stop offset="0" stop-color="#0f3f63"/><stop offset="1" stop-color="#3a8ec6"/></linearGradient></defs><polygon points="0,0 280,0 140,48" fill="url(#flap)"/><polyline points="0,110 140,58 280,110" fill="none" stroke="var(--fold)"/></svg>
    <div class="brand-mark"><span class="dot"></span>Brivosta</div>
  </section>

  <section class="item envelope-back back-white">
    <svg width="280" height="120" aria-hidden="true"><polyline points="0,0 140,44 280,0" fill="none" stroke="var(--fold)"/><polyline points="0,120 140,58 280,120" fill="none" stroke="var(--fold)"/></svg>
    <p class="web small">www.BrivostaFilms.com</p>
  </section>
</main>
</body>
</html>
```